Song Cover Art. Song Tittle Lift The Floor

I would like a design for my songs. I'm a producer and i prouder EDM music such as Big Room House / Electro House music. Currently i have a new songs tittle name Lift The Floor and i need a cover art for my songs. I'm not sure what design i have in mind right now and i would like someone to create it for me. My DJ name is DJ Vex.
Reason: Hey, i will give sometimes for you guys to create the design for me. Please do zorvix edm cover art or brenlow - lift the floor.
Target Market(s)
Electronic Dance Music Lovers
Industry/Entity Type
House
Look and feel
Each slider illustrates characteristics of the customer's brand and the style your logo design should communicate.

```html
<!DOCTYPE html>
<html lang="en">
<head>
<meta charset="utf-8">
<title>Lift The Floor — Cover Art</title>
<link rel="stylesheet" href="https://fonts.googleapis.com/css2?family=Krona+One&display=swap">
<style>
  :root {
    --sky-top: #b9a7bd;
    --sky-mid: #d8c3cf;
    --peak: #6f6470;
    --mist: #c9bcc6;
    --water: #b49aa8;
    --water-deep: #8e7585;
    --title-faint: rgba(150, 160, 140, 0.75);
    --title-dark: #151417;
    --title-glitch: #8a2b7c;
    --magenta: #d23ad8;
    --teal: #3fd3c8;
    --teal-soft: rgba(63, 211, 200, 0.55);
    --frame-faint: rgba(120, 112, 122, 0.7);
  }
  html, body {
    margin: 0;
    padding: 0;
    overflow: hidden;
    background: #ffffff;
  }
  .cover {
    width: 1200px;
    height: 848px;
    display: block;
  }
  .cover-title {
    font-family: "Krona One", "Arial Black", sans-serif;
    font-size: 118px;
  }
  .title-lift { fill: var(--title-faint); }
  .title-the { fill: var(--title-dark); opacity: 0.9; }
  .title-floor { fill: var(--title-glitch); }
  .title-floor-shadow { fill: var(--title-dark); opacity: 0.55; }
</style>
</head>
<body>
<svg class="cover" viewBox="0 0 1200 848" xmlns="http://www.w3.org/2000/svg">
  <defs>
    <linearGradient id="landscape-tone" x1="0" y1="0" x2="0" y2="1">
      <stop offset="0" stop-color="var(--sky-top)"/>
      <stop offset="0.22" stop-color="var(--sky-mid)"/>
      <stop offset="0.38" stop-color="var(--peak)"/>
      <stop offset="0.55" stop-color="var(--peak)"/>
      <stop offset="0.64" stop-color="var(--mist)"/>
      <stop offset="0.8" stop-color="var(--water)"/>
      <stop offset="1" stop-color="var(--water-deep)"/>
    </linearGradient>
  </defs>

  <rect class="backdrop-photo" x="0" y="0" width="1200" height="848"
        fill="url(#landscape-tone)" role="img"
        aria-label="Misty mountain range at dusk reflected in a still lake, in lavender and pink tones"/>

  <polygon class="frame-triangle-faint" points="580,90 215,770 960,770"
           fill="rgba(255,255,255,0.06)" stroke="var(--frame-faint)" stroke-width="5"/>

  <g class="glitch-bands">
    <rect x="0" y="560" width="1200" height="40" fill="var(--teal)" opacity="0.8"/>
    <rect x="0" y="636" width="1200" height="24" fill="var(--teal-soft)"/>
    <rect x="0" y="668" width="1200" height="14" fill="var(--teal-soft)" opacity="0.6"/>
  </g>

  <g class="glitch-slices">
    <rect x="880" y="584" width="320" height="10" fill="var(--magenta)" opacity="0.6"/>
    <rect x="880" y="604" width="240" height="8" fill="#6a6f8a" opacity="0.7"/>
    <rect x="900" y="620" width="300" height="12" fill="var(--magenta)" opacity="0.45"/>
    <rect x="870" y="646" width="180" height="8" fill="#5d5f80" opacity="0.7"/>
    <rect x="1040" y="590" width="6" height="84" fill="#5d5f80" opacity="0.5"/>
    <rect x="1080" y="590" width="6" height="84" fill="#5d5f80" opacity="0.5"/>
    <rect x="1120" y="590" width="6" height="84" fill="#5d5f80" opacity="0.5"/>
  </g>

  <g class="cover-title">
    <text class="title-lift" x="290" y="255" textLength="600" lengthAdjust="spacingAndGlyphs">LIFT</text>
    <text class="title-the" x="290" y="465" textLength="600" lengthAdjust="spacingAndGlyphs">THE</text>
    <text class="title-floor-shadow" x="296" y="673" textLength="600" lengthAdjust="spacingAndGlyphs">FLOOR</text>
    <text class="title-floor" x="290" y="668" textLength="600" lengthAdjust="spacingAndGlyphs">FLOOR</text>
  </g>

  <polygon class="frame-triangle-accent" points="630,100 240,770 990,770"
           fill="none" stroke="var(--magenta)" stroke-width="7" stroke-linejoin="miter"/>
</svg>
</body>
</html>
```